Vantrelle Stationary Design

We're seeking a fresh and modern design for our stationery that captures the essence of our Real Estate brand. The current design, while functional, lacks visual appeal. We're looking for a more attractive and engaging design that showcases our professionalism and expertise in the real estate industry. I am attaching the current letter head and an image with a letter "P" as logo.

Target Market(s)

Real Estate Sales and Rentals

Industry/Entity Type

Real Estate

Requirements
Nice to have
• The owner seems to like the letter "P"

```html
<!DOCTYPE html>
<html lang="en">
<head>
<meta charset="utf-8">
<title>Vantrelle Stationery</title>
<link rel="stylesheet" href="https://fonts.googleapis.com/css2?family=Raleway:wght@400;600;700&family=Montserrat:wght@800&family=Open+Sans:wght@400;600&display=swap">
<style>
  :root {
    --navy: #373a62;
    --navy-deep: #23284f;
    --yellow: #f1cb3c;
    --ink: #2b2b2b;
    --rule: #9a9a9a;
    --paper: #ffffff;
    --backdrop: #ffffff;
  }
  * { margin: 0; padding: 0; box-sizing: border-box; }
  html, body { width: 1200px; height: 800px; overflow: hidden; background: var(--backdrop); }
  .canvas { position: relative; width: 1200px; height: 800px; }

  .brand { display: flex; align-items: center; gap: 5px; font-family: "Raleway", sans-serif; font-weight: 700; text-transform: uppercase; letter-spacing: 0.5px; }
  .brand-mark { display: inline-block; }

  /* Letterhead */
  .letterhead { position: absolute; left: 110px; top: 152px; width: 380px; height: 490px; background: var(--paper); border: 1px solid #e4e4e4; overflow: hidden; }
  .letterhead .brand { position: absolute; right: 22px; top: 24px; color: var(--navy); font-size: 19px; }
  .letterhead .brand-mark { width: 11px; height: 11px; background: var(--navy); }
  .subject { position: absolute; left: 25px; top: 140px; font-family: "Montserrat", sans-serif; font-weight: 800; font-size: 12.5px; letter-spacing: 1.6px; color: var(--ink); }
  .body-lines { position: absolute; left: 25px; top: 172px; width: 320px; }
  .body-lines span { display: block; height: 3px; background: var(--rule); margin-bottom: 7.4px; }
  .body-lines .gap { background: none; height: 3px; margin-bottom: 14px; }
  .signature { position: absolute; right: 40px; top: 370px; width: 122px; }
  .signature span { display: block; margin-left: auto; height: 2px; margin-bottom: 5px; background: var(--rule); }
  .signature .name-line { height: 2.5px; background: var(--ink); width: 122px; }
  .letter-footer { position: absolute; left: 0; bottom: 0; width: 100%; height: 56px; }
  .letter-footer svg { position: absolute; left: 0; top: 0; }
  .letter-footer .footer-mark { position: absolute; left: 14px; top: -14px; width: 20px; height: 20px; background: var(--navy); }
  .contact { font-family: "Open Sans", sans-serif; font-size: 5.8px; line-height: 1.4; }
  .contact strong { font-weight: 600; }
  .letter-footer .contact { position: absolute; left: 37px; top: 8px; color: var(--navy-deep); }

  /* Notebook */
  .notebook { position: absolute; left: 583px; top: 153px; width: 276px; height: 368px; background: linear-gradient(200deg, var(--navy) 0%, var(--navy-deep) 60%, #2c3058 100%); }
  .notebook .brand { position: absolute; left: 40px; top: 36px; color: var(--paper); font-size: 19px; }
  .notebook .brand-mark { width: 11px; height: 11px; background: var(--yellow); }
  .notebook .contact { position: absolute; left: 37px; bottom: 19px; color: var(--paper); }

  /* Business cards */
  .card { position: absolute; left: 903px; width: 194px; height: 112px; }
  .card-front { top: 231px; background: var(--paper); border: 1px solid #8a8a8a; overflow: hidden; }
  .card-front .strip { position: absolute; left: 0; top: 0; width: 43px; height: 100%; background: var(--yellow); }
  .card-front .card-mark { position: absolute; left: 27px; top: 16px; width: 32px; height: 32px; background: var(--navy); }
  .person { position: absolute; left: 71px; top: 22px; font-family: "Montserrat", sans-serif; font-weight: 800; color: var(--ink); }
  .person .full-name { font-size: 11px; letter-spacing: 1.4px; }
  .person .title { font-size: 6px; letter-spacing: 0.9px; margin-top: -1px; }
  .card-lines { position: absolute; left: 71px; top: 52px; }
  .card-row { display: flex; align-items: center; gap: 6px; height: 15px; }
  .card-row .bars span { display: block; height: 1.6px; background: var(--ink); margin: 2px 0; }
  .card-back { top: 354px; background: var(--navy); display: flex; align-items: center; justify-content: center; }
  .card-back .brand { color: var(--paper); font-size: 17px; }
  .card-back .brand-mark { width: 10px; height: 10px; background: var(--yellow); }

  /* Standalone brand */
  .brand-large { position: absolute; left: 858px; top: 655px; color: var(--navy); font-size: 46px; gap: 12px; letter-spacing: 1px; }
  .brand-large .brand-mark { width: 30px; height: 30px; background: var(--navy); }
</style>
</head>
<body>
<main class="canvas">

  <section class="letterhead">
    <div class="brand"><span class="brand-mark"></span>Vantrelle</div>
    <h2 class="subject">Subject Title Space Here</h2>
    <div class="body-lines">
      <span style="width:305px;margin-left:15px"></span>
      <span></span><span></span><span></span><span></span>
      <span style="width:44px"></span>
      <span class="gap"></span>
      <span></span><span></span><span></span>
      <span style="width:110px"></span>
      <span class="gap"></span>
      <span></span><span></span><span></span>
      <span style="width:69px"></span>
    </div>
    <div class="signature">
      <span style="width:62px"></span>
      <span class="name-line"></span>
      <span style="width:72px"></span>
    </div>
    <footer class="letter-footer">
      <svg width="380" height="56" viewBox="0 0 380 56" aria-hidden="true">
        <rect x="0" y="7" width="380" height="32" fill="var(--yellow)"/>
        <polygon points="380,7 380,56 245,56" fill="var(--navy)"/>
      </svg>
      <span class="footer-mark"></span>
      <p class="contact">480 Harborview Lane, Suite 6, Larkfield, MA 02198<br>
        <strong>Phone : 555-014-2286 &nbsp;|&nbsp; Fax: 555-014-7730</strong><br>
        <strong>Vantrellepropertysolutions.com</strong></p>
    </footer>
  </section>

  <section class="notebook">
    <div class="brand"><span class="brand-mark"></span>Vantrelle</div>
    <p class="contact">480 Harborview Lane, Suite 6, Larkfield, MA 02198<br>
      <strong>Phone : 555-014-2286 &nbsp;|&nbsp; Fax: 555-014-7730</strong><br>
      <strong>Vantrellepropertysolutions.com</strong></p>
  </section>

  <section class="card card-front">
    <div class="strip"></div>
    <span class="card-mark"></span>
    <div class="person">
      <div class="full-name">Name Surname</div>
      <div class="title">Business Title</div>
    </div>
    <div class="card-lines">
      <div class="card-row">
        <svg width="8" height="6" viewBox="0 0 8 6" aria-hidden="true"><rect x="0.4" y="0.4" width="7.2" height="5.2" fill="none" stroke="var(--ink)" stroke-width="0.8"/><path d="M0.4 0.4 L4 3.4 L7.6 0.4" fill="none" stroke="var(--ink)" stroke-width="0.8"/></svg>
        <div class="bars"><span style="width:78px"></span></div>
      </div>
      <div class="card-row">
        <svg width="8" height="9" viewBox="0 0 8 9" aria-hidden="true"><path d="M4 8.6 C1.5 5.5 0.6 4.2 0.6 3.2 A3.4 3.4 0 0 1 7.4 3.2 C7.4 4.2 6.5 5.5 4 8.6Z" fill="none" stroke="var(--ink)" stroke-width="0.9"/><circle cx="4" cy="3.2" r="1.1" fill="var(--ink)"/></svg>
        <div class="bars"><span style="width:50px"></span><span style="width:78px"></span></div>
      </div>
      <div class="card-row">
        <svg width="8" height="8" viewBox="0 0 8 8" aria-hidden="true"><path d="M1.6 0.6 L3 2.4 L2.2 3.4 C2.8 4.6 3.6 5.4 4.7 5.9 L5.6 5 L7.4 6.4 L6.5 7.6 C3.6 7.2 0.9 4.6 0.5 1.6Z" fill="var(--ink)"/></svg>
        <div class="bars"><span style="width:68px"></span><span style="width:68px"></span></div>
      </div>
    </div>
  </section>

  <section class="card card-back">
    <div class="brand"><span class="brand-mark"></span>Vantrelle</div>
  </section>

  <div class="brand brand-large"><span class="brand-mark"></span>Vantrelle</div>

</main>
</body>
</html>
```